This is for Torvendigo ONLY Business Card Text Revisions

Hello, Torvendigo. Please see the attachment. It contains the new text needed. You already have the design itself, the one you created in project 2806514. Thank you.

```html
<!DOCTYPE html>
<html lang="en">
<head>
<meta charset="utf-8">
<title>Harborline Venue Partners – Business Card</title>
<link href="https://fonts.googleapis.com/css2?family=Cormorant+SC:wght@500;600;700&family=Open+Sans:wght@400;600;700&display=swap" rel="stylesheet">
<style>
  :root {
    --navy: #14265c;
    --rule-gray: #a3a3a3;
    --text-gray: #555555;
    --title-gray: #868686;
    --paper: #ffffff;
  }
  html, body {
    margin: 0;
    padding: 0;
    width: 1200px;
    height: 693px;
    overflow: hidden;
    background: var(--paper);
  }
  .card {
    position: relative;
    width: 1200px;
    height: 693px;
    background: var(--paper);
    overflow: hidden;
  }
  .edge-band {
    position: absolute;
    left: 0; top: 0;
    width: 80px; height: 693px;
    background: var(--navy);
  }
  .edge-rule {
    position: absolute;
    left: 85px; top: 0;
    width: 6px; height: 693px;
    background: var(--rule-gray);
  }
  .brand-mark {
    position: absolute;
    left: 159px; top: 93px;
    width: 158px; height: 158px;
    background: var(--navy);
  }
  .brand-divider {
    position: absolute;
    left: 332px; top: 90px;
    width: 3px; height: 160px;
    background: var(--rule-gray);
  }
  .brand-name {
    position: absolute;
    left: 350px; top: 104px;
    margin: 0;
    font-family: "Cormorant SC", serif;
    font-weight: 600;
    font-size: 50px;
    line-height: 42px;
    color: var(--navy);
    letter-spacing: 1px;
  }
  .address {
    position: absolute;
    left: 161px; top: 344px;
    margin: 0;
    font-family: "Open Sans", sans-serif;
    font-style: normal;
    font-size: 27px;
    line-height: 39px;
    color: var(--text-gray);
  }
  .person {
    position: absolute;
    right: 67px; top: 316px;
    text-align: right;
    font-family: "Cormorant SC", serif;
  }
  .person-name {
    margin: 0;
    font-weight: 700;
    font-size: 48px;
    line-height: 48px;
    color: var(--navy);
    letter-spacing: 1.5px;
  }
  .person-title {
    margin: 0;
    font-weight: 600;
    font-size: 33px;
    line-height: 37px;
    color: var(--title-gray);
    letter-spacing: 1.5px;
  }
  .contact {
    position: absolute;
    left: 161px; top: 497px;
    margin: 0;
    font-family: "Open Sans", sans-serif;
    font-size: 27px;
    line-height: 47px;
    color: var(--text-gray);
  }
  .contact-label {
    font-weight: 700;
    color: var(--navy);
  }
</style>
</head>
<body>
  <div class="card">
    <div class="edge-band"></div>
    <div class="edge-rule"></div>

    <div class="brand-mark"></div>
    <div class="brand-divider"></div>
    <p class="brand-name">Harborline<br>Venue<br>Partners, llc</p>

    <address class="address">214 Larkspur Bend,<br>Cedar Hollow, TX 78000</address>

    <div class="person">
      <p class="person-name">Dana Whitcomb</p>
      <p class="person-title">Vice President</p>
      <p class="person-title">Event Sourcing &amp; Contracting</p>
    </div>

    <p class="contact">
      <span class="contact-label">Phone :</span> 555-014-0192<br>
      dwhitcomb@harborlinevenuepartners.com<br>
      www.harborlinevenuepartners.com/sourcing
    </p>
  </div>
</body>
</html>
```